Business Card and Word .doc header and footer required

I need a business card designed for my cybersecurity consulting company. Also required, is a header and footer to be ued for my word documents.
Attached is the Logo design, font and rgb used.

Industry/Entity Type

Cyber Security Consulting

Contact Information for Business Card

Name, Phone, email, website

Colors
0054AA
0677BA
7BADD7
CADEEF
E8F1F8

Requirements
Must have
• Sleek, modern

```html
<!DOCTYPE html>
<html lang="en">
<head>
<meta charset="utf-8">
<title>Harwell Ridge Consulting – Letterhead</title>
<link href="https://fonts.googleapis.com/css2?family=Montserrat:wght@400;600&display=swap" rel="stylesheet">
<style>
  :root {
    --ink: #1b1f3a;
    --text: #151515;
    --brand: #0677ba;
    --brand-light: #7badd7;
    --paper: #ffffff;
  }
  * { margin: 0; padding: 0; box-sizing: border-box; }
  html, body { width: 927px; height: 1200px; overflow: hidden; background: var(--paper); }
  .letterhead {
    position: relative;
    width: 927px;
    height: 1200px;
    background: var(--paper);
    font-family: "Montserrat", sans-serif;
    color: var(--text);
  }
  .brand {
    position: absolute;
    top: 20px;
    left: 0;
    width: 100%;
    display: flex;
    flex-direction: column;
    align-items: center;
    gap: 18px;
  }
  .brand-dot {
    width: 76px;
    height: 76px;
    border-radius: 50%;
    background: var(--brand);
  }
  .brand-name {
    font-weight: 600;
    font-size: 22px;
    letter-spacing: 0.5px;
    color: var(--ink);
  }
  .contact-row {
    position: absolute;
    top: 1076px;
    left: 0;
    width: 100%;
    height: 24px;
    font-size: 17px;
  }
  .contact-item {
    position: absolute;
    top: 0;
    display: flex;
    align-items: center;
    height: 24px;
    white-space: nowrap;
  }
  .contact-item svg { flex: none; }
  .contact-phone { left: 80px; gap: 11px; }
  .contact-email { left: 289px; gap: 17px; }
  .contact-web { left: 582px; gap: 13px; }
  .address {
    position: absolute;
    top: 1124px;
    left: 0;
    width: 100%;
    text-align: center;
    font-size: 17px;
    white-space: pre;
  }
</style>
</head>
<body>
  <div class="letterhead">
    <header class="brand">
      <div class="brand-dot"></div>
      <div class="brand-name">HARWELL RIDGE CONSULTING</div>
    </header>

    <footer>
      <div class="contact-row">
        <div class="contact-item contact-phone">
          <svg width="23" height="23" viewBox="0 0 24 24" aria-hidden="true">
            <path fill="var(--brand)" d="M6.6 2.5l2.7 3.6c.4.5.3 1.2-.1 1.6L7.6 9.2c.9 2.5 4.1 5.9 6.9 7.1l1.6-1.6c.5-.4 1.2-.5 1.7-.1l3.5 2.7c.5.4.6 1.1.2 1.6l-1.9 2.4c-.6.7-1.6 1-2.5.7C10 19.4 4.8 14 2.6 7.4c-.3-.9 0-1.9.7-2.5l2-1.9c.4-.5 1-.5 1.3-.5z"/>
            <path fill="none" stroke="var(--brand)" stroke-width="1.6" stroke-linecap="round" d="M14 2.5a7.5 7.5 0 0 1 7.5 7.5M14 6a4 4 0 0 1 4 4"/>
          </svg>
          <span>028-415 730 962</span>
        </div>
        <div class="contact-item contact-email">
          <svg width="25" height="18" viewBox="0 0 25 18" aria-hidden="true">
            <rect x="0" y="0" width="25" height="18" fill="var(--brand)"/>
            <path d="M0.5 0.8L12.5 10.5L24.5 0.8M0.5 17.2L9.5 8.5M24.5 17.2L15.5 8.5" fill="none" stroke="var(--brand-light)" stroke-width="1.2"/>
          </svg>
          <span>info@harwellrc.com</span>
        </div>
        <div class="contact-item contact-web">
          <svg width="20" height="20" viewBox="0 0 20 20" aria-hidden="true">
            <circle cx="10" cy="10" r="9" fill="none" stroke="var(--brand)" stroke-width="1.8"/>
            <path fill="var(--brand)" d="M6 4.5c1.6-.6 3 .1 3.4 1.3.3 1-.6 1.6-1.5 2-.9.4-.7 1.5.2 1.9 1.2.5 1.1 1.8.5 2.9-.6 1-.4 2.3-.8 3.4C5.6 15 3.7 12.6 3.6 10 3.4 7.6 4.4 5.6 6 4.5zM12.5 9.5c1.2-.3 2.5.2 3 1.3.4 1.2-.3 2.6-1.3 3.5-.8.6-1.6.2-1.6-.8 0-1-.9-1.3-1-2.2 0-.9.2-1.6.9-1.8z"/>
          </svg>
          <span>www.harwellridge.com</span>
        </div>
      </div>
      <p class="address">318, Kestrel Park Road  Northbrook, 60214</p>
    </footer>
  </div>
</body>
</html>
```